Quillbrook Builders Business Cards

I want to use the logo and make an unique business card that shows the textured Logo with brick and builings. I want to be able to stand out when I pass out business cards.

```html
<!DOCTYPE html>
<html lang="en">
<head>
<meta charset="utf-8">
<title>Quillbrook Builders Business Cards</title>
<link href="https://fonts.googleapis.com/css2?family=Arimo:wght@400;700&family=Roboto+Condensed:wght@500&display=swap" rel="stylesheet">
<style>
  :root {
    --backdrop: #5a5a5a;
    --brick: #c4421f;
    --brick-deep: #9c321c;
    --paper: #ffffff;
    --rule: #6e6e6e;
    --ink-navy: #1f2a44;
    --text-light: #ffffff;
  }
  * { margin: 0; padding: 0; box-sizing: border-box; }
  html, body {
    width: 1200px; height: 1200px; overflow: hidden;
    background: var(--backdrop);
    font-family: "Arimo", Arial, sans-serif;
  }
  .canvas { position: relative; width: 1200px; height: 1200px; }
  .card { position: absolute; width: 690px; height: 394px; overflow: hidden; }
  .card-front { left: 266px; top: 158px; background: var(--paper); }
  .card-back {
    left: 262px; top: 652px;
    background: radial-gradient(ellipse at 50% 50%, var(--brick) 0%, var(--brick-deep) 100%);
  }
  .front-band {
    position: absolute; left: 0; top: 222px; width: 100%; height: 172px;
    background: radial-gradient(ellipse at 55% 30%, #d04620 0%, var(--brick-deep) 100%);
  }
  .front-rule {
    position: absolute; left: 0; top: 222px; width: 100%; height: 5px;
    background: linear-gradient(90deg, #4a4a4a, #9a9a9a 50%, #4a4a4a);
    border-bottom: 1px solid #fff;
  }
  .brand-name {
    position: absolute; left: 0; width: 100%; text-align: center;
    font-weight: 700; letter-spacing: 1px; text-transform: uppercase;
  }
  .card-front .brand-name { top: 90px; font-size: 30px; color: var(--brick); }
  .card-back .brand-name { top: 160px; font-size: 40px; color: var(--text-light); }
  .tagline {
    position: absolute; left: 0; width: 100%; text-align: center;
    font-family: "Roboto Condensed", "Arial Narrow", sans-serif; font-weight: 500;
    color: var(--ink-navy);
  }
  .card-front .tagline { top: 182px; font-size: 9.5px; }
  .card-back .tagline { top: 288px; font-size: 15px; }
  .identity {
    position: absolute; right: 335px; top: 268px; text-align: right;
    color: var(--text-light); font-size: 16px; line-height: 21px;
  }
  .identity .person-name { font-size: 25px; font-weight: 700; line-height: 30px; letter-spacing: 0.5px; }
  .identity .person-title { margin-top: 0; }
  .divider {
    position: absolute; left: 370px; top: 268px; width: 1px; height: 94px;
    background: rgba(255,255,255,0.8);
  }
  .contacts {
    position: absolute; left: 388px; top: 278px; list-style: none;
    color: var(--text-light); font-size: 16px;
  }
  .contacts li { display: flex; align-items: center; height: 20.7px; }
  .contacts svg { width: 13px; height: 13px; margin-right: 13px; fill: var(--text-light); }
</style>
</head>
<body>
<div class="canvas">

  <section class="card card-front">
    <div class="brand-name">Quillbrook Builders</div>
    <div class="tagline">Patios - Sidewalks - Retaining Walls - Foundations</div>
    <div class="front-band"></div>
    <div class="front-rule"></div>
    <div class="identity">
      <div class="person-name">DANIEL HARPER</div>
      <div class="person-title">President</div>
      <div>412 Larkspur Road</div>
      <div>Fernvale, Canada 20817</div>
    </div>
    <div class="divider"></div>
    <ul class="contacts">
      <li><svg viewBox="0 0 24 24"><path d="M6.6 10.8a15 15 0 0 0 6.6 6.6l2.2-2.2c.3-.3.7-.4 1-.2 1.1.4 2.3.6 3.6.6.6 0 1 .4 1 1V20c0 .6-.4 1-1 1A17 17 0 0 1 3 4c0-.6.4-1 1-1h3.5c.6 0 1 .4 1 1 0 1.3.2 2.5.6 3.6.1.3 0 .7-.2 1z"/></svg>555-214-7780</li>
      <li><svg viewBox="0 0 24 24"><path d="M7 1h10a2 2 0 0 1 2 2v18a2 2 0 0 1-2 2H7a2 2 0 0 1-2-2V3a2 2 0 0 1 2-2zm0 3v15h10V4z"/></svg>555-318-9046</li>
      <li><svg viewBox="0 0 24 24"><path d="M2 5h20v14H2zm2 2v.5l8 5.5 8-5.5V7zm0 3v7h16v-7l-8 5.5z"/></svg>info@quillbrookbuilders.com</li>
      <li><svg viewBox="0 0 24 24"><path d="M12 2a10 10 0 1 0 0 20 10 10 0 0 0 0-20zm-1 17.9A8 8 0 0 1 4.2 10.2L9 15v1a2 2 0 0 0 2 2zm6.9-2.5A2 2 0 0 0 16 16h-1v-3a1 1 0 0 0-1-1H8v-2h2a1 1 0 0 0 1-1V7h2a2 2 0 0 0 2-2v-.4a8 8 0 0 1 2.9 12.8z"/></svg>www.quillbrookbuilders.com</li>
    </ul>
  </section>

  <section class="card card-back">
    <div class="brand-name">Quillbrook Builders</div>
    <div class="tagline">Patios - Sidewalks - Retaining Walls - Foundations</div>
  </section>

</div>
</body>
</html>
```